Business card

creative business card for newly created national firm that specializes in high-density storage for retail markets. Looking for creativity and overall theme that will differentiate from others in this unique niche ...essentially a design that will provide instant recognition as we develop our identity in the marketplace. possible initial thoughts are attached with logo separately

Retail

```html
<!DOCTYPE html>
<html lang="en">
<head>
<meta charset="UTF-8">
<title>Dense Stock Group — Business Card</title>
<link rel="stylesheet" href="https://fonts.googleapis.com/css2?family=Montserrat:ital,wght@0,400;0,700;1,400&family=Tinos:ital@1&display=swap">
<style>
  :root {
    --sky-panel: #b9e0f6;
    --card-white: #ffffff;
    --brand-blue: #2f7fa3;
    --mark-blue: #3d9fcf;
    --ink: #0d0d0d;
    --slate-teal: #2d5468;
  }
  html, body {
    margin: 0;
    padding: 0;
    width: 1200px;
    height: 720px;
    overflow: hidden;
    background: var(--card-white);
  }
  .card {
    position: relative;
    width: 1200px;
    height: 720px;
    display: flex;
    font-family: "Montserrat", sans-serif;
  }
  .brand-panel {
    position: relative;
    width: 561px;
    height: 100%;
    background: var(--sky-panel);
  }
  .brand-square {
    position: absolute;
    left: 262px;
    top: 78px;
    width: 250px;
    height: 250px;
    background: var(--mark-blue);
  }
  .brand-name {
    position: absolute;
    left: 62px;
    top: 410px;
    margin: 0;
    font-family: "Montserrat", sans-serif;
    font-weight: 400;
    font-size: 76px;
    line-height: 80px;
    letter-spacing: 1px;
    color: var(--brand-blue);
  }
  .brand-name span { display: block; }
  .contact-side {
    flex: 1;
    position: relative;
    text-align: center;
  }
  .person-name {
    position: absolute;
    left: 0; right: 0;
    top: 185px;
    margin: 0;
    font-weight: 700;
    font-size: 43px;
    letter-spacing: 1px;
    color: var(--ink);
  }
  .phone {
    position: absolute;
    left: 0; right: 0;
    top: 240px;
    margin: 0;
    font-weight: 400;
    font-size: 31px;
    color: var(--ink);
  }
  .tagline {
    position: absolute;
    left: 0; right: 0;
    top: 390px;
    margin: 0;
    font-family: "Tinos", serif;
    font-style: italic;
    font-size: 39px;
    color: var(--slate-teal);
  }
  .website {
    position: absolute;
    left: 0; right: 0;
    top: 535px;
    margin: 0;
    font-style: italic;
    font-size: 25px;
    color: var(--ink);
  }
</style>
</head>
<body>
  <main class="card">
    <section class="brand-panel">
      <div class="brand-square" aria-hidden="true"></div>
      <h1 class="brand-name"><span>DENSE</span><span>STOCK</span><span>GROUP</span></h1>
    </section>
    <section class="contact-side">
      <h2 class="person-name">DANA WHITLOW</h2>
      <p class="phone">855-STACK-UP</p>
      <p class="tagline">Innovate your space</p>
      <p class="website">www.densestockgroup.com</p>
    </section>
  </main>
</body>
</html>
```